Save the date: email notification

I need a "Save the Date" email notification design for my wedding:

Objetives:

1.- to notify friends about our future wedding ( by sending an email)
2.- to request our friends to send us their phisical address. ( reply to the email)

It will not be the formal invitation for the wedding, just an announcement.

Wedding Date: 15-sep-2012
Our names: Lucía & Rodrigo

Target Market(s)

friends, family and other commitments

Industry/Entity Type

Wedding

Requirements
Must have
• Wedding Date: 15-sep-2012
Our names: Lucía & Rodrigo

```html
<!DOCTYPE html>
<html lang="es">
<head>
<meta charset="utf-8">
<title>Save the Date · Lucía + Rodrigo</title>
<link rel="stylesheet" href="https://fonts.googleapis.com/css2?family=Lato:wght@300&family=Libre+Baskerville:wght@400;700&display=swap">
<style>
  :root {
    --paper: #ffffff;
    --navy: #063a5a;
    --seafoam: #adc9c5;
    --ink-light: #ffffff;
    --sans: "Lato", "Helvetica Neue", Arial, sans-serif;
    --serif: "Libre Baskerville", Georgia, serif;
  }
  * { margin: 0; padding: 0; box-sizing: border-box; }
  html, body {
    width: 1029px;
    height: 1200px;
    overflow: hidden;
    background: var(--paper);
  }
  .card {
    position: relative;
    width: 1029px;
    height: 1200px;
    background: var(--paper);
  }
  .band {
    position: absolute;
    left: 73px;
    width: 884px;
    background: var(--navy);
  }
  .band--top { top: 55px; height: 67px; }
  .band--bottom { top: 1075px; height: 65px; }
  .panel {
    position: absolute;
    left: 73px;
    top: 122px;
    width: 884px;
    height: 953px;
    background: var(--seafoam);
  }
  .flourish {
    position: absolute;
    left: 305px;
    width: 414px;
    display: block;
  }
  .flourish--top { top: 212px; height: 56px; }
  .flourish--bottom { top: 670px; height: 46px; }
  .line {
    position: absolute;
    left: 0;
    width: 100%;
    text-align: center;
    color: var(--ink-light);
    white-space: nowrap;
  }
  .month {
    top: 280px;
    font-family: var(--sans);
    font-weight: 300;
    font-size: 64px;
    letter-spacing: 3px;
    line-height: 1;
  }
  .day {
    top: 318px;
    font-family: var(--serif);
    font-weight: 400;
    font-size: 400px;
    line-height: 1;
    letter-spacing: -10px;
  }
  .headline {
    top: 742px;
    font-family: var(--sans);
    font-weight: 300;
    font-size: 52px;
    letter-spacing: 3px;
    line-height: 1;
  }
  .couple {
    top: 788px;
    font-family: var(--serif);
    font-weight: 700;
    font-size: 54px;
    line-height: 1.1;
    letter-spacing: -1px;
  }
  .couple .plus { color: var(--navy); }
  .announce {
    top: 862px;
    font-family: var(--sans);
    font-weight: 300;
    font-size: 36px;
    letter-spacing: 2px;
    line-height: 1;
  }
  .reply {
    top: 934px;
    font-family: var(--serif);
    font-weight: 400;
    font-size: 17px;
    line-height: 1;
  }
</style>
</head>
<body>
  <main class="card">
    <div class="band band--top"></div>
    <section class="panel" aria-label="Save the date"></section>
    <div class="band band--bottom"></div>

    <svg class="flourish flourish--top" viewBox="0 0 414 56" role="img" aria-label="Decorative calligraphic flourish">
      <rect x="0" y="14" width="414" height="28" rx="14" fill="var(--navy)" opacity="0.55"/>
    </svg>

    <p class="line month">SEPTEMBER</p>
    <p class="line day">15</p>

    <svg class="flourish flourish--bottom" viewBox="0 0 414 46" role="img" aria-label="Decorative calligraphic flourish">
      <rect x="0" y="9" width="414" height="28" rx="14" fill="var(--navy)" opacity="0.55"/>
    </svg>

    <p class="line headline">SAVE THE DATE</p>
    <p class="line couple">lucía<span class="plus">+</span>rodrigo</p>
    <p class="line announce">ARE GETTING MARRIED!</p>
    <p class="line reply">Please, reply to this e-mail sending your address</p>
  </main>
</body>
</html>
```